Website design for a hair building fibre

Hi I’m needing a website made for both men and women to purchase the product is a hair building fibre that you apply to thinning hair to make your hair look really thick I’ll need the website to be easy to use professional and also very classy I will need it to work with moss quill vel dor and credit cards I’ll need to have the CEO words and everything ready so I can sell I don’t have photos that I want to put on there so I’ll need a website designer to assist me in having the beautiful photos on there I know very little about websites so I need someone to be able to do it all for me

I can only provide photos of the colours of the products
I believe there will be 8 colours to sell as well
I’ve uploaded a photo of the logo I’d really like it if the website designer can check other competitors website so my website does not look like theres, I don’t want my website to look like a copied website of the competitors I’m located in Australia.
I’m also looking for someone who can open up a Wendoral and Pluvestra page and then can unload photos on them ready for consumers to view and buy.

```html
<!DOCTYPE html>
<html lang="en">
<head>
<meta charset="utf-8">
<title>Fullmane – Hair Building Fibre</title>
<link href="https://fonts.googleapis.com/css2?family=Poppins:ital,wght@0,300;0,400;0,500;0,600;1,300;1,400&family=Dancing+Script:wght@500&display=swap" rel="stylesheet">
<style>
:root{
  --navy:#1b2433;
  --navy-2:#222c3c;
  --sky:#7ec8e3;
  --sky-dark:#5fb3d3;
  --ink:#1e1e1e;
  --muted:#6b6b6b;
  --card:#f3f3f4;
  --paper:#ffffff;
  --mist:#e7eef5;
  --feature:#f1f4f7;
  --foot:#e9e9ea;
  --gold:#f2b705;
}
*{box-sizing:border-box;margin:0;padding:0}
html,body{width:1200px;height:4680px;overflow:hidden}
body{font-family:"Poppins",sans-serif;color:var(--ink);background:var(--paper);position:relative}
section,header{position:relative;width:1200px;overflow:hidden}
.abs{position:absolute}
a{color:inherit;text-decoration:none}

/* top bar */
.topbar{height:31px;background:var(--sky);display:flex;align-items:center;justify-content:center;gap:8px;font-size:13px;color:var(--navy)}

/* nav */
.nav{height:73px;background:var(--navy);color:#fff}
.brand{color:var(--sky);font-weight:300;letter-spacing:1px}
.nav .brand{left:100px;top:12px;font-size:30px;line-height:32px}
.nav .brand small{display:block;font-size:12px;letter-spacing:2.5px;line-height:16px}
.nav-links{left:360px;top:0;height:73px;display:flex;align-items:center;gap:0;font-size:14px;font-weight:500}
.nav-links a{position:relative;margin-right:46px}
.nav-links a.active{color:var(--sky)}
.nav-links a.active::after{content:"";position:absolute;left:0;right:0;bottom:-26px;height:3px;background:var(--sky)}
.search{left:865px;top:24px;width:150px;height:26px;border-bottom:1px solid #8894a6;display:flex;align-items:center;gap:8px;font-size:11px;color:#c6ccd6}
.nav-icons{left:1022px;top:24px;display:flex;gap:14px}

/* hero */
.hero{height:625px;background:linear-gradient(110deg,#3d5a69 0%,#4a7688 45%,#3a6576 100%)}
.hero-photo{right:0;top:0;width:640px;height:625px;background:linear-gradient(160deg,#2d9cbf 0%,#2a5f73 35%,#3b4e59 70%,#30414b 100%)}
.hero-text{left:100px;top:192px;color:#fff}
.hero-text h1{font-size:72px;font-weight:500;line-height:72px;letter-spacing:1px}
.hero-text h2{font-size:38px;font-weight:500;line-height:44px}
.hero-text p{font-size:17px;line-height:30px;margin-top:16px;max-width:420px;color:#eef4f7}
.btn{display:inline-flex;align-items:center;justify-content:center;gap:12px;font-size:14px;font-weight:600;border-radius:0 22px 22px 0;height:40px}
.btn-sky{background:var(--sky);color:var(--navy)}
.btn-dark{background:var(--navy);color:#fff}
.hero .btn{left:100px;top:393px;width:184px}
.follow{left:100px;top:580px;font-size:12px;color:#fff;display:flex;gap:10px}
.mouse{left:588px;top:562px}
.scroll-line{left:599px;top:599px;width:1.5px;height:160px;background:var(--sky);z-index:3}
.pager{left:1140px;top:205px;color:#fff;font-size:12px;display:flex;flex-direction:column;align-items:center;gap:8px}
.pager .bar{width:1.5px;height:140px;background:rgba(255,255,255,.7)}

/* product grids */
.sec-title{width:100%;text-align:center;font-weight:300;font-size:40px;letter-spacing:.5px;color:var(--ink)}
.sec-sub{width:100%;text-align:center;font-size:16px;line-height:27px;color:var(--muted)}
.grid{left:100px;display:flex;gap:18px}
.card{width:236px}
.card .media{position:relative;height:295px;background:var(--card);border-radius:4px}
.card .media .shot{position:absolute;left:60px;top:35px;width:116px;height:190px;border-radius:10px;background:linear-gradient(180deg,#3a3a3e,#141416)}
.card .media .shot.round{left:48px;top:55px;width:140px;height:140px;border-radius:50%}
.card .media .shot.comb{left:30px;top:75px;width:176px;height:120px;border-radius:10px 10px 60px 60px}
.badge{position:absolute;left:20px;top:-6px;background:#fff;font-size:10px;font-weight:600;padding:2px 16px;border-radius:2px;box-shadow:0 1px 2px rgba(0,0,0,.08)}
.badge.right{left:auto;right:120px}
.stars{position:absolute;left:0;right:0;bottom:14px;text-align:center;font-size:17px;letter-spacing:2px;color:#222}
.card h3{font-size:17px;font-weight:600;margin-top:12px}
.price{font-size:15px;font-weight:600;margin-top:6px}
.price s{font-size:12px;font-weight:400;color:#9a9a9a;margin-left:12px}
.card .btn{width:184px;margin-top:16px}
.arrow-btn{width:34px;height:34px;border:1.5px solid #333;border-radius:50%;display:flex;align-items:center;justify-content:center}

/* about */
.about{height:564px;background:radial-gradient(circle at 70% 30%,#253044,var(--navy) 70%)}
.frame{left:100px;top:91px;width:424px;height:370px;border:1.5px solid #d7dde6;border-right:none;border-bottom:none;border-radius:18px 0 0 18px}
.about-photo{left:118px;top:109px;width:458px;height:370px;border-radius:0 36px 0 36px;background:linear-gradient(135deg,#8a8f96,#c9ccd0 55%,#a4a8ad)}
.about-text{left:658px;top:108px;width:445px;color:#e9edf3}
.about-text h2{font-size:44px;font-weight:300;color:#fff;margin-bottom:20px}
.about-text p{font-size:15.5px;line-height:27.5px;margin-bottom:12px}
.about .btn{left:658px;top:434px;width:184px}

/* direct */
.direct{height:467px;background:linear-gradient(120deg,#f1f0ee,#e2e1df 50%,#ecebe9)}
.direct h2{left:91px;top:140px;width:524px;text-align:center;font-size:30px;font-weight:400;letter-spacing:.5px}
.direct .lead{left:91px;top:188px;width:524px;text-align:center;font-size:13px;padding-bottom:6px;border-bottom:1.5px solid #555}
.discount{left:91px;top:232px;width:524px;text-align:center;font-size:26px}
.discount em{font-family:"Dancing Script",cursive;font-style:normal;font-size:40px}
.direct .btn{left:238px;top:293px;width:231px;font-size:14px}
.direct-shot{left:420px;top:27px;width:780px;height:400px;background:radial-gradient(ellipse at 55% 75%,#6d5645 0%,#3b3431 30%,rgba(40,40,40,.15) 60%,transparent 72%)}

/* result */
.result{height:600px;background:var(--mist)}
.quote{left:100px;top:188px;width:350px;font-style:italic;font-weight:300;font-size:17.5px;line-height:29.5px;color:#333}
.who{left:100px;top:420px}
.who b{font-size:20px;font-weight:500}
.who span{display:block;font-size:14px;color:#555}
.who i{display:block;font-style:normal;color:var(--gold);font-size:18px;letter-spacing:1px}
.before{left:507px;top:155px;width:278px;height:366px;background:linear-gradient(180deg,#c8cbd0,#e8e8e6 40%,#aeb7c2)}
.after{left:818px;top:155px;width:204px;height:266px;background:linear-gradient(180deg,#c9cdd2,#e7e7e5 45%,#9fb1c6)}
.tag{position:absolute;left:4px;top:2px;font-family:Georgia,serif;font-weight:700;font-size:16px;color:#222}
.after .tag{font-size:13px}

/* join */
.join{height:373px;background:var(--navy);color:#fff}
.mail-ring{left:105px;top:88px;width:102px;height:102px;border-radius:50%;background:#dfe6ee;border:5px solid #6c7b90;display:flex;align-items:center;justify-content:center}
.join h2{left:231px;top:92px;font-size:42px;font-weight:400;line-height:50px}
.join h3{left:231px;top:152px;font-size:24px;font-weight:300}
.join .note{left:742px;top:98px;width:300px;font-size:13px;line-height:23px;color:#dfe4ea}
.field{top:238px;height:49px;width:324px;background:#fff;border-radius:0 25px 25px 0;display:flex;align-items:center;gap:10px;padding-left:22px;font-size:13px;color:#444}
.join .subscribe{left:798px;top:238px;width:187px;height:49px;font-size:14px;border-radius:0 25px 25px 0}

/* features */
.features{height:218px;background:var(--feature)}
.feature{top:60px;width:230px;text-align:center}
.feature svg{display:block;margin:0 auto 10px}
.feature h4{font-size:16px;font-weight:500}
.feature p{font-size:12.5px;line-height:20px;color:#444;margin-top:4px}

/* footer */
.footer{height:273px;background:#fff}
.footer .brand{left:100px;top:82px;font-size:40px;line-height:40px}
.footer .brand small{display:block;font-size:16px;letter-spacing:2.5px;line-height:22px}
.socials{left:100px;top:148px;display:flex;gap:10px}
.socials span{display:flex;align-items:center;gap:4px;font-size:11px;color:var(--ink)}
.socials span::before{content:"";width:10px;height:10px;border:1.5px solid var(--ink);border-radius:50%}
.col{top:60px}
.col h5{font-size:16px;font-weight:500;margin-bottom:8px;letter-spacing:.5px}
.col li{list-style:none;font-size:14px;line-height:30px;color:#333}
.cards{display:flex;gap:6px;margin-top:10px}
.cards span{width:48px;height:30px;border-radius:3px;background:#e5e9ef;font-size:10px;font-weight:500;display:flex;align-items:center;justify-content:center;color:var(--navy)}
.copyright{height:62px;background:var(--foot);display:flex;align-items:center;justify-content:center;font-size:14px;color:#333}
</style>
</head>
<body>

<div class="topbar">
  <svg width="16" height="12" viewBox="0 0 16 12"><path d="M1 1h9v7H1z M10 4h3l2 3v1h-5z" fill="#1b2433"/><circle cx="4" cy="10" r="1.6" fill="#1b2433"/><circle cx="12" cy="10" r="1.6" fill="#1b2433"/></svg>
  <span>Get free shipping on order $50+</span>
</div>

<header class="nav">
  <div class="abs brand">FULLMANE<small>HAIR BUILDING FIBRE</small></div>
  <nav class="abs nav-links">
    <a class="active" href="#">HOME</a><a href="#">ABOUT</a><a href="#">PRODUCTS</a><a href="#">BLOG</a><a href="#">CONACT</a>
  </nav>
  <div class="abs search">
    <svg width="18" height="18" viewBox="0 0 18 18"><circle cx="7.5" cy="7.5" r="6" stroke="#fff" stroke-width="1.6" fill="none"/><path d="M12 12l5 5" stroke="#fff" stroke-width="1.6"/></svg>
    <span>Search</span>
  </div>
  <div class="abs nav-icons">
    <svg width="20" height="20" viewBox="0 0 20 20"><path d="M10 17S2 12 2 7a4 4 0 0 1 8-1 4 4 0 0 1 8 1c0 5-8 10-8 10z" stroke="#fff" stroke-width="1.5" fill="none"/></svg>
    <svg width="20" height="20" viewBox="0 0 20 20"><circle cx="10" cy="6" r="4" stroke="#fff" stroke-width="1.5" fill="none"/><path d="M2 19c1-5 15-5 16 0" stroke="#fff" stroke-width="1.5" fill="none"/></svg>
    <svg width="24" height="22" viewBox="0 0 24 22"><path d="M3 7h14l-1 12H4z M7 7V5a3 3 0 0 1 6 0v2" stroke="#fff" stroke-width="1.5" fill="none"/><circle cx="18" cy="16" r="5" fill="#7ec8e3"/><text x="18" y="19" font-size="7" text-anchor="middle" fill="#1b2433" font-family="Poppins,sans-serif">0</text></svg>
  </div>
</header>

<section class="hero">
  <div class="abs hero-photo" role="img" aria-label="Portrait of a man with thick styled hair in a dark t-shirt against a teal wall"></div>
  <div class="abs hero-text">
    <h1>FULLMANE</h1>
    <h2>HAIR BUILDING FIBRE</h2>
    <p>At vero eos et accusamus et ito odio dignissimos ducimus qui blanditiis praesentium</p>
  </div>
  <a class="abs btn btn-sky" href="#">ORDER NOW
    <svg width="26" height="10" viewBox="0 0 26 10"><path d="M0 5h24M19 1l5 4-5 4" stroke="#1b2433" stroke-width="1.6" fill="none"/></svg></a>
  <div class="abs follow"><span>Follow Us :</span><span>Wendoral</span><span>Chirpel</span><span>Linkora</span></div>
  <svg class="abs mouse" width="24" height="36" viewBox="0 0 24 36"><rect x="2" y="2" width="20" height="30" rx="10" stroke="#fff" stroke-width="1.6" fill="none"/><path d="M12 9v6" stroke="#fff" stroke-width="1.6"/></svg>
  <div class="abs pager"><span style="transform:rotate(90deg)">01</span><div class="bar"></div><span style="transform:rotate(90deg)">04</span>
    <svg width="10" height="22" viewBox="0 0 10 22"><path d="M1 6l4-4 4 4M1 16l4 4 4-4" stroke="#fff" stroke-width="1.4" fill="none"/></svg></div>
</section>
<div class="abs scroll-line" style="top:703px;height:62px"></div>

<section style="height:716px">
  <h2 class="abs sec-title" style="top:83px">OUR PRODUCTS</h2>
  <p class="abs sec-sub" style="top:136px">At vero eos et accusamus et iusto odio digos ducimus qui blanditiis praesentium<br>voluptatum deleniti atque corrupti quos dolores</p>
  <div class="abs arrow-btn" style="left:45px;top:361px"><svg width="12" height="14" viewBox="0 0 12 14"><path d="M9 1L3 7l6 6" stroke="#333" stroke-width="1.6" fill="none"/></svg></div>
  <div class="abs arrow-btn" style="left:1117px;top:361px"><svg width="12" height="14" viewBox="0 0 12 14"><path d="M3 1l6 6-6 6" stroke="#333" stroke-width="1.6" fill="none"/></svg></div>
  <div class="abs grid" style="top:215px">
    <article class="card"><div class="media"><span class="badge">SALE !</span><div class="shot" role="img" aria-label="Jar of hair building fibre"></div><div class="stars">★★★★★</div></div><h3>Finibus Bonorum et</h3><p class="price">$ 28.00<s>$ 35.00</s></p><a class="btn btn-dark" href="#">SHOP NOW <svg width="26" height="10" viewBox="0 0 26 10"><path d="M0 5h24M19 1l5 4-5 4" stroke="#fff" stroke-width="1.6" fill="none"/></svg></a></article>
    <article class="card"><div class="media"><span class="badge">SALE !</span><div class="shot" role="img" aria-label="Jar of hair building fibre"></div><div class="stars">★★★★★</div></div><h3>Finibus Bonorum et</h3><p class="price">$ 28.00<s>$ 35.00</s></p><a class="btn btn-dark" href="#">SHOP NOW <svg width="26" height="10" viewBox="0 0 26 10"><path d="M0 5h24M19 1l5 4-5 4" stroke="#fff" stroke-width="1.6" fill="none"/></svg></a></article>
    <article class="card"><div class="media"><span class="badge">SALE !</span><div class="shot round" role="img" aria-label="Spray applicator nozzle"></div><div class="stars">★★★★★</div></div><h3>Finibus Bonorum et</h3><p class="price">$ 28.00<s>$ 35.00</s></p><a class="btn btn-dark" href="#">SHOP NOW <svg width="26" height="10" viewBox="0 0 26 10"><path d="M0 5h24M19 1l5 4-5 4" stroke="#fff" stroke-width="1.6" fill="none"/></svg></a></article>
    <article class="card"><div class="media"><span class="badge">SALE !</span><div class="shot" role="img" aria-label="Jar of hair building fibre"></div><div class="stars">★★★★★</div></div><h3>Finibus Bonorum et</h3><p class="price">$ 28.00<s>$ 35.00</s></p><a class="btn btn-dark" href="#">SHOP NOW <svg width="26" height="10" viewBox="0 0 26 10"><path d="M0 5h24M19 1l5 4-5 4" stroke="#fff" stroke-width="1.6" fill="none"/></svg></a></article>
  </div>
</section>

<section class="about">
  <div class="abs frame"></div>
  <div class="abs about-photo" role="img" aria-label="Man examining his thinning hairline"></div>
  <div class="abs about-text">
    <h2>ABOUT US</h2>
    <p>At vero eos et accuso dignissimos ducimus qui blanditiis praesentium voluptatum dti atque corrupti quos dolores et quas molestias excepturi siti cupiditate non provident, similique sunt in culpa qui officia deserunt mollitia animi, id est laborum et dolorum fuga.</p>
    <p>Et harum quidem rerum facilis &nbsp;et expedita disnctio. Nam libero tempore, cum solutabis est eligendi optio cumque nihil impedit quo minus id quod maxime</p>
  </div>
  <a class="abs btn btn-sky" href="#">LEARN MORE <svg width="26" height="10" viewBox="0 0 26 10"><path d="M0 5h24M19 1l5 4-5 4" stroke="#1b2433" stroke-width="1.6" fill="none"/></svg></a>
</section>

<section class="direct">
  <div class="abs direct-shot" role="img" aria-label="Fibre jars, spray bottle, applicator and hairline comb on a pile of fibre powder"></div>
  <h2 class="abs">DIRECT SELLING ADVANTAGE</h2>
  <p class="abs lead">Take advantage of our 30% discount on the entire range through our direct sales</p>
  <p class="abs discount">30% <em>Discount</em></p>
  <a class="abs btn btn-dark" href="#">TO THE PRODUCTS <svg width="26" height="10" viewBox="0 0 26 10"><path d="M0 5h24M19 1l5 4-5 4" stroke="#fff" stroke-width="1.6" fill="none"/></svg></a>
</section>

<section style="height:678px">
  <h2 class="abs sec-title" style="top:85px">BEST SELLERS</h2>
  <div class="abs arrow-btn" style="left:46px;top:347px"><svg width="12" height="14" viewBox="0 0 12 14"><path d="M9 1L3 7l6 6" stroke="#333" stroke-width="1.6" fill="none"/></svg></div>
  <div class="abs arrow-btn" style="left:1118px;top:347px"><svg width="12" height="14" viewBox="0 0 12 14"><path d="M3 1l6 6-6 6" stroke="#333" stroke-width="1.6" fill="none"/></svg></div>
  <div class="abs grid" style="top:175px;left:101px">
    <article class="card"><div class="media"><div class="shot round" role="img" aria-label="Spray applicator nozzle"></div><div class="stars">★★★★★</div></div><h3>Finibus Bonorum et</h3><p class="price">$ 28.00<s>$ 35.00</s></p><a class="btn btn-dark" href="#">SHOP NOW <svg width="26" height="10" viewBox="0 0 26 10"><path d="M0 5h24M19 1l5 4-5 4" stroke="#fff" stroke-width="1.6" fill="none"/></svg></a></article>
    <article class="card"><div class="media"><span class="badge" style="left:25px">30% OFF</span><div class="shot comb" role="img" aria-label="Hairline optimizer comb"></div><div class="stars">★★★★★</div></div><h3>Finibus Bonorum et</h3><p class="price">$ 28.00<s>$ 35.00</s></p><a class="btn btn-dark" href="#">SHOP NOW <svg width="26" height="10" viewBox="0 0 26 10"><path d="M0 5h24M19 1l5 4-5 4" stroke="#fff" stroke-width="1.6" fill="none"/></svg></a></article>
    <article class="card"><div class="media"><div class="shot" role="img" aria-label="Jar of hair building fibre"></div><div class="stars">★★★★★</div></div><h3>Finibus Bonorum et</h3><p class="price">$ 28.00<s>$ 35.00</s></p><a class="btn btn-dark" href="#">SHOP NOW <svg width="26" height="10" viewBox="0 0 26 10"><path d="M0 5h24M19 1l5 4-5 4" stroke="#fff" stroke-width="1.6" fill="none"/></svg></a></article>
    <article class="card"><div class="media"><span class="badge" style="left:25px">40% OFF</span><div class="shot" role="img" aria-label="Jar of hair building fibre"></div><div class="stars">★★★★★</div></div><h3>Finibus Bonorum et</h3><p class="price">$ 28.00<s>$ 35.00</s></p><a class="btn btn-dark" href="#">SHOP NOW <svg width="26" height="10" viewBox="0 0 26 10"><path d="M0 5h24M19 1l5 4-5 4" stroke="#fff" stroke-width="1.6" fill="none"/></svg></a></article>
  </div>
</section>

<section class="result">
  <h2 class="abs sec-title" style="top:72px">REAL PEOPLE REAL RESULT</h2>
  <p class="abs quote">"At vero eos et accusato odio dignissimos ducimus qui itiis praesentium voluptatum deleniti atque corrti quos dolores et quas molestias excep sint occaecati cupiditate non provident, similique sunt in culpa qui officia deseruntlitia animi, id est laborum et dolorum fuga. "</p>
  <div class="abs who"><b>-Ravi Calder</b><span>Finibus Bonorum et</span><i>★★★★★</i></div>
  <div class="abs before" role="img" aria-label="Young man before treatment, side view of thinning hair"><span class="tag">BEFORE</span></div>
  <div class="abs after" role="img" aria-label="Same young man after treatment with fuller hair"><span class="tag">AFTER</span></div>
  <svg class="abs" style="left:818px;top:448px" width="96" height="14" viewBox="0 0 96 14"><path d="M2 7h32M8 2L2 7l6 5" stroke="#222" stroke-width="2" fill="none"/><path d="M60 7h32M86 2l6 5-6 5" stroke="#222" stroke-width="2" fill="none"/></svg>
</section>

<section class="join">
  <div class="abs mail-ring"><svg width="46" height="46" viewBox="0 0 46 46"><path d="M5 18l18-13 18 13v22H5z" stroke="#1b2433" stroke-width="2" fill="none"/><path d="M5 18l18 13 18-13" stroke="#1b2433" stroke-width="2" fill="none"/><circle cx="23" cy="17" r="6" stroke="#1b2433" stroke-width="2" fill="none"/></svg></div>
  <h2 class="abs">JOIN NOW &amp; GET 10%</h2>
  <h3 class="abs">OFF YOUR NEXT PURCHASE!</h3>
  <p class="abs note">*Online only, First-time subscribers only. Returning subscribers will be resubscribed for marketing/promo emails.</p>
  <div class="abs field" style="left:100px"><svg width="14" height="14" viewBox="0 0 14 14"><circle cx="7" cy="4" r="3" stroke="#444" fill="none"/><path d="M1 13c1-5 11-5 12 0" stroke="#444" fill="none"/></svg>Your Name*</div>
  <div class="abs field" style="left:453px"><svg width="14" height="12" viewBox="0 0 14 12"><rect x="1" y="1" width="12" height="10" stroke="#444" fill="none"/><path d="M1 1l6 5 6-5" stroke="#444" fill="none"/></svg>Your Email*</div>
  <a class="abs btn btn-sky subscribe" href="#"><svg width="16" height="14" viewBox="0 0 16 14"><path d="M1 6L15 1 11 13 8 8z" fill="#1b2433"/></svg>SUBSCRIBE</a>
</section>

<section class="features">
  <div class="abs feature" style="left:96px"><svg width="64" height="42" viewBox="0 0 64 42"><rect x="6" y="6" width="32" height="24" stroke="#1b2433" stroke-width="2" fill="none"/><rect x="10" y="12" width="22" height="9" fill="#7ec8e3"/><path d="M38 14h12l8 8v8H38z" stroke="#1b2433" stroke-width="2" fill="none"/><circle cx="16" cy="34" r="4" stroke="#1b2433" stroke-width="2" fill="#fff"/><circle cx="48" cy="34" r="4" stroke="#1b2433" stroke-width="2" fill="#fff"/></svg><h4>FREE SHIPPING</h4><p>At vero eos et accusamus iusto odio dignissimos ducimus qi</p></div>
  <div class="abs feature" style="left:358px"><svg width="48" height="42" viewBox="0 0 48 42"><rect x="8" y="3" width="24" height="32" stroke="#1b2433" stroke-width="2" fill="none"/><path d="M13 11h14M13 17h14M13 23h8" stroke="#1b2433" stroke-width="2"/><circle cx="34" cy="30" r="8" stroke="#1b2433" stroke-width="2" fill="#7ec8e3"/></svg><h4>RETURNS</h4><p>At vero eos et accusamus iusto odio dignissimos ducimus qi</p></div>
  <div class="abs feature" style="left:618px"><svg width="48" height="42" viewBox="0 0 48 42"><path d="M10 22a14 14 0 0 1 28 0" stroke="#1b2433" stroke-width="2" fill="none"/><rect x="6" y="20" width="8" height="12" rx="3" stroke="#1b2433" stroke-width="2" fill="#7ec8e3"/><rect x="34" y="20" width="8" height="12" rx="3" stroke="#1b2433" stroke-width="2" fill="#7ec8e3"/><path d="M38 32c0 5-6 7-12 7" stroke="#1b2433" stroke-width="2" fill="none"/></svg><h4>ONLINE SUPPORT</h4><p>At vero eos et accusamus iusto odio dignissimos ducimus qi</p></div>
  <div class="abs feature" style="left:878px"><svg width="54" height="42" viewBox="0 0 54 42"><rect x="4" y="6" width="36" height="24" rx="2" stroke="#1b2433" stroke-width="2" fill="none"/><path d="M4 13h36" stroke="#1b2433" stroke-width="3"/><path d="M38 22l9 3v6c0 5-4 8-9 9-5-1-9-4-9-9v-6z" stroke="#1b2433" stroke-width="2" fill="#7ec8e3"/></svg><h4>FLEXIBLE PAYMENT</h4><p>At vero eos et accusamus iusto odio dignissimos ducimus qi</p></div>
</section>

<footer>
  <section class="footer">
    <div class="abs brand">FULLMANE<small>HAIR BUILDING FIBRE</small></div>
    <div class="abs socials"><span>Wendoral</span><span>Chirpel</span><span>Linkora</span><span>Pluvestra</span></div>
    <div class="abs col" style="left:349px"><h5>QUICK LINKS</h5><ul><li>Home</li><li>About</li><li>Proudct</li><li>Blog</li><li>Contact</li></ul></div>
    <div class="abs col" style="left:520px"><h5>HELP</h5><ul><li>Faq</li><li>Shipping &amp; returns</li><li>Contact us</li><li>Accessibility</li></ul></div>
    <div class="abs col" style="left:702px"><h5>OTHERS</h5><ul><li>Terms &amp; conditions</li><li>Privacy policy</li><li>Site map</li></ul></div>
    <div class="abs col" style="left:885px"><h5>CONTACT</h5><ul><li>+1 555-010-2040</li><li>info@fullmanefibre.com</li></ul>
      <div class="cards"><span>Paytrove</span><span>Circlo</span><span>Vantra</span><span>Amerix</span></div></div>
  </section>
  <div class="copyright">©Copyright ©2022 Fullmane Hair Building Fibre. All Rights Reserved.</div>
</footer>

</body>
</html>
```